Cedar Steam & Sauna Digital Billboard

This is a digital billboard so we are looking for a fresh design that will capture people's attention. The current billboard is a simple black text "#FeelTheWarmth" over a white background with a picture of an iphone with one of our photos (Reference attached) We enjoy how clean and simple this design is, but open to other concepts. Since the weather is getting colder, a lot of people come to our spa because we offer various dry saunas and hot baths in addition to our spa services. We have a few photos for reference on our website information view www.cedarsteamhouse.com , but you can email me for additional photo content - moreno@cedarsteamhouse.com

Target Market(s)

New Jersey Locals

Colors
0255a3
ec1f27
f37122
ffc214

Requirements
Must have
• Font is "Barlow"
Nice to have
• #FeelTheWarmth hashtag

```html
<!DOCTYPE html>
<html lang="en">
<head>
<meta charset="utf-8">
<title>Cedar Steam &amp; Sauna — Billboard</title>
<link rel="stylesheet" href="https://fonts.googleapis.com/css2?family=Cinzel:wght@400;500&family=Open+Sans:wght@400&display=swap">
<style>
  :root {
    --stage: #5f6160;
    --board: #ffffff;
    --ink: #111111;
    --brand-teal: #49bccb;
    --wood-deep: #5a2c14;
    --wood-mid: #a4562a;
    --wood-glow: #e39a5a;
    --ember-dark: #2e1710;
    --ember-mid: #8a4526;
    --ember-glow: #d98a56;
  }
  * { margin: 0; padding: 0; box-sizing: border-box; }
  html, body { width: 1200px; height: 1200px; overflow: hidden; }
  body { background: var(--stage); position: relative; }

  .billboard {
    position: absolute;
    left: 30px; top: 434px;
    width: 1140px; height: 332px;
    background: var(--board);
    overflow: hidden;
  }

  .photo { position: absolute; top: 0; height: 100%; }
  .photo--left {
    left: 0; width: 340px;
    background:
      linear-gradient(to right, rgba(255,255,255,0) 62%, var(--board) 100%),
      linear-gradient(100deg, var(--wood-deep) 0%, var(--wood-mid) 30%, var(--wood-glow) 52%, var(--wood-mid) 75%, var(--wood-deep) 100%);
  }
  .photo--right {
    right: 0; width: 240px;
    background:
      linear-gradient(to left, rgba(255,255,255,0) 58%, var(--board) 100%),
      linear-gradient(80deg, var(--ember-glow) 0%, var(--ember-mid) 45%, var(--ember-dark) 100%);
  }

  .content {
    position: absolute;
    left: 300px; width: 572px; top: 0; height: 100%;
    text-align: center;
    color: var(--ink);
  }

  .brand {
    position: absolute; top: 44px; left: 0; width: 100%;
    display: flex; align-items: center; justify-content: center; gap: 10px;
    font-family: "Cinzel", serif; font-weight: 500;
    font-size: 22px; letter-spacing: 0.5px;
  }
  .brand__dot {
    width: 20px; height: 20px; border-radius: 50%;
    background: var(--brand-teal);
  }

  .headline {
    position: absolute; top: 112px; left: -40px; width: calc(100% + 80px);
    font-family: "Cinzel", serif; font-weight: 400;
    font-size: 56px; line-height: 1; letter-spacing: 1px;
  }
  .tagline {
    position: absolute; top: 218px; left: -40px; width: calc(100% + 80px);
    font-family: "Cinzel", serif; font-weight: 500;
    font-size: 22px; letter-spacing: 0.8px;
  }
  .website {
    position: absolute; top: 274px; left: 0; width: 100%;
    display: flex; align-items: center; justify-content: center; gap: 8px;
    font-family: "Open Sans", sans-serif;
    font-size: 21px; letter-spacing: 1.5px;
  }
  .website svg { width: 17px; height: 17px; }
</style>
</head>
<body>
  <section class="billboard">
    <div class="photo photo--left" role="img" aria-label="Guest sitting cross-legged in a warm-lit cedar sauna facing slatted windows"></div>
    <div class="photo photo--right" role="img" aria-label="Guest relaxing in a glowing sauna with eyes closed"></div>

    <div class="content">
      <div class="brand"><span class="brand__dot"></span>Cedar Steam &amp; Sauna</div>
      <h1 class="headline">#FeelTheWarmth</h1>
      <p class="tagline">We offer various dry saunas and hot baths</p>
      <p class="website">
        <svg viewBox="0 0 20 20" aria-hidden="true">
          <g fill="none" stroke="#111" stroke-width="1.4">
            <circle cx="10" cy="10" r="8.5"/>
            <ellipse cx="10" cy="10" rx="3.8" ry="8.5"/>
            <line x1="1.5" y1="10" x2="18.5" y2="10"/>
            <line x1="3" y1="5.5" x2="17" y2="5.5"/>
            <line x1="3" y1="14.5" x2="17" y2="14.5"/>
          </g>
        </svg>
        www.cedarsteamhouse.com
      </p>
    </div>
  </section>
</body>
</html>
```